Old Fashioned, Artisan Goat Milk Soap Label

We are branching out in our goat milk dairy into artisan goat milk soaps. High quality, yet an old fashioned feel. Simple yet elegant. Emphasis on the milk and its moisturizing, healing, softening, and superiority.
Purity in a simple design that harkens back to a quaint, earlier time where quality ingredients were valued as much as quality workmanship.
Perhaps a drop symbolizing the milk, or a bucket pouring into or out of the logo. We already have our farm logo, Willowbrook Hollow, and were thinking the soap would be "Sweet Nell"
The labels will grace our liquid soap bottles and our bar soaps. 3.5" X 2.5"
The label color will be an antiqued ivory or other shade to convey a simpler time.

Reason: Realized that the contest length was short enough to scare away designers. Adding time to give entered designers time to create.

Target Market(s)

Upscale people looking to know where their products come from. People looking for better options, artisan products.

Requirements
Must have
• My project must have emphasis on the milk, old time feel, simple elegance
Nice to have
• Perhaps a drop symbolizing the milk, or a bucket pouring into or out of the logo. We already have our farm logo, Willowbrook Hollow, and were thinking the soap would be "Sweet Nell"
• If you use a goat, please be aware that we have the breed Nubians that have long luxurious ears and don't have horns.

```html
<!DOCTYPE html>
<html lang="en">
<head>
<meta charset="utf-8">
<title>Sweet Nell Goat Milk Soap Label</title>
<link rel="stylesheet" href="https://fonts.googleapis.com/css2?family=Cinzel:wght@400&family=Raleway:wght@400;600&display=swap">
<style>
  :root {
    --page: #f4f4f2;
    --kraft: #ebe2d5;
    --kraft-speck: #d6cbbb;
    --band: #e3c6a3;
    --slate: #9d9d9b;
    --ink: #4a3c3a;
    --navy: #2c3a5c;
    --soft-ink: #5a5552;
    --goat-light: #f1ebe3;
    --goat-mid: #b9b3ad;
  }
  * { margin: 0; padding: 0; box-sizing: border-box; }
  html, body {
    width: 721px;
    height: 1200px;
    overflow: hidden;
    background: var(--page);
  }
  .label {
    position: absolute;
    left: 40px;
    top: 325px;
    width: 640px;
    height: 549px;
    background-color: var(--kraft);
    background-image:
      radial-gradient(var(--kraft-speck) 0.8px, transparent 1.2px),
      radial-gradient(var(--kraft-speck) 0.6px, transparent 1px);
    background-size: 23px 19px, 31px 27px;
    background-position: 3px 5px, 14px 11px;
    overflow: hidden;
  }
  .label-shapes {
    position: absolute;
    inset: 0;
    width: 100%;
    height: 100%;
  }
  .farm-name {
    position: absolute;
    top: 32px;
    left: 0;
    width: 100%;
    text-align: center;
    font-family: "Cinzel", serif;
    font-weight: 400;
    font-size: 26px;
    letter-spacing: 2px;
    color: var(--navy);
  }
  .product-name {
    position: absolute;
    left: 36px;
    top: 84px;
    font-family: "Cinzel", serif;
    font-weight: 400;
    font-size: 58px;
    letter-spacing: 1px;
    color: var(--ink);
    white-space: nowrap;
  }
  .product-type {
    position: absolute;
    left: 38px;
    top: 166px;
    font-family: "Raleway", sans-serif;
    font-weight: 400;
    font-size: 21px;
    color: var(--soft-ink);
  }
  .goat-art {
    position: absolute;
    left: 460px;
    top: 112px;
    width: 160px;
    height: 218px;
    border-radius: 50% 50% 30% 30%;
    background: radial-gradient(ellipse at 50% 45%, var(--goat-light) 0%, var(--goat-mid) 100%);
    opacity: 0.85;
  }
  .tagline {
    position: absolute;
    left: 36px;
    top: 402px;
    font-family: "Raleway", sans-serif;
    font-weight: 600;
    font-size: 16px;
    color: var(--ink);
    white-space: nowrap;
  }
</style>
</head>
<body>
  <div class="label">
    <svg class="label-shapes" viewBox="0 0 385 330" preserveAspectRatio="none" aria-hidden="true">
      <polygon class="slate-strip" fill="var(--slate)"
        points="0,38 8,36 14,39 21,36 27,39 32,37 32,305 0,305"/>
      <polygon class="torn-band" fill="var(--band)"
        points="0,45 60,44 140,46 220,43 300,45 325,44 328,60 324,90 330,120 326,150 329,180 325,215 327,238 260,241 180,238 100,241 30,239 0,240"/>
    </svg>
    <div class="farm-name">Willowbrook Hollow</div>
    <h1 class="product-name">SWEET NELL</h1>
    <p class="product-type">goat milk soaps</p>
    <div class="goat-art" role="img" aria-label="Line illustration of a resting Nubian goat kid with long ears"></div>
    <p class="tagline">moisturizing, healing, softening, and superiority.</p>
  </div>
</body>
</html>
```